Brightbuns Business Card Design

Our company is called Brightbuns. We manufacture confectionary snacks & frozen novelties. Our initial product portfolio includes frozen ice lollies/popsicles & stick ice cream bars.

We require a business card design.

Please use the attached Logo.

Please use an orange, brown, yellow colour code. You may choose any combination of the 3 or include all three. The logo however must remain orange.

Target Market(s)

Business card will be targeted at distributors of our products such as supermarket procurement managers, convenience store owners, wholesale distributors and merchandising agents.

Industry/Entity Type

Business

Requirements
Must have
• Kelvin Marsh_Director/ P.O.Box Westhollow 5172, Accra, Ghana / m: 00233(0)507318264/ e: kelvin.marsh@fernpost.co.uk

```html
<!DOCTYPE html>
<html lang="en">
<head>
<meta charset="utf-8">
<title>Brightbuns Business Card</title>
<link rel="stylesheet" href="https://fonts.googleapis.com/css2?family=Archivo+Narrow:wght@400;700&display=swap">
<style>
  :root {
    --backdrop: #d6d6d6;
    --card-orange: #ea6c1f;
    --panel-white: #fbfbfb;
    --rim-yellow: #f5c523;
    --text-brown: #4a2a12;
    --text-orange: #ea6c1f;
  }
  html, body {
    margin: 0;
    width: 1200px;
    height: 900px;
    overflow: hidden;
    background: var(--backdrop);
  }
  .business-card {
    position: absolute;
    left: 180px;
    top: 210px;
    width: 840px;
    height: 480px;
    background: var(--card-orange);
    font-family: "Archivo Narrow", "Arial Narrow", sans-serif;
  }
  .oval-panel {
    position: absolute;
    inset: 0;
  }
  .card-content {
    position: absolute;
    inset: 0;
    display: flex;
    flex-direction: column;
    align-items: center;
    text-align: center;
  }
  .brand {
    margin-top: 78px;
    display: flex;
    align-items: center;
    gap: 14px;
  }
  .brand-dot {
    width: 46px;
    height: 46px;
    border-radius: 50%;
    background: var(--text-orange);
  }
  .brand-name {
    font-size: 66px;
    font-weight: 700;
    color: var(--text-orange);
    line-height: 1;
  }
  .person-name {
    margin-top: 42px;
    font-size: 36px;
    font-weight: 700;
    color: var(--text-brown);
    line-height: 1.1;
  }
  .person-role {
    font-size: 30px;
    color: var(--text-brown);
    line-height: 1.2;
  }
  .contact-list {
    margin-top: 20px;
    font-size: 27px;
    color: var(--text-orange);
    line-height: 1.32;
  }
  .contact-list p { margin: 0; }
</style>
</head>
<body>
  <div class="business-card">
    <svg class="oval-panel" width="840" height="480" viewBox="0 0 840 480" aria-hidden="true">
      <ellipse cx="420" cy="240" rx="386" ry="208" fill="var(--panel-white)" stroke="var(--rim-yellow)" stroke-width="11"/>
    </svg>
    <div class="card-content">
      <div class="brand">
        <span class="brand-dot"></span>
        <span class="brand-name">Brightbuns</span>
      </div>
      <div class="person-name">Kelvin Marsh</div>
      <div class="person-role">Director</div>
      <div class="contact-list">
        <p>P.O.Box Westhollow 5172, Accra, Ghana</p>
        <p>m: 00233(0)507318264</p>
        <p>e: kelvin.marsh@fernpost.co.uk</p>
      </div>
    </div>
  </div>
</body>
</html>
```